Flyer Design

Hi, This work has potential to expand! After the flyers I could be looking to improve my website design and our van needs brandingPlease find attached what I would like (or if you can improve the design) on the front of my flyer. I will also provide pictures for the back. I am not sure how I want this laid out. (i have attached a picture called idea, I like this for some reason but might not work for me) My husband is young (32) and we have built a website (www.stonvale.co.uk) but we haven't gone fully live yet as he is still working for someone elseAnyway, I want to set him apart from all the rest. I want vibrant colors which is eye catchy and interesting. Makes people want to read it and not put the flyer in the binThe reason these pictures are more about conservatories, patios (smaller building work) is becasue these first lot of flyers are aimed at a new build site with 1000 homes per site. They will only be looking for conservatoies, driveways, small alterations. Maybe the conservatory could be in the middle? Again, I don't know please stick to the logo which is on the bottom left of my design but the rest is up to you. I also had a little play with the brick in the logo to maybe make it a background design somewhere. Might be rubbish ideaI did not get any help with the website so if the Flyers take the branding/colours in a different direction/theme there could be work to go forward with continuous improvement on the website AND we want to brand the vanI look forward to seeing your deignThank you for your help!Maribel
Updates
Project Deadline Extended Reason: Thank you for your efforts so far. My husband and I are reviewing the flyers and it's harder to chose the design that we like than we thought. I hope to improve the brief and interact with you more as I think we know have a better understanding of what we are looking forI will improve the brief in the next 24 hoursKind regardsSaoirse Added Saturday, January 31, 2015
Industry/Entity Type
Building
Look and feel

```html
<!DOCTYPE html>
<html lang="en">
<head>
<meta charset="utf-8">
<title>Stonvale Building Services – Flyer</title>
<link rel="stylesheet" href="https://fonts.googleapis.com/css2?family=Lilita+One&family=Open+Sans:wght@400;600;700&display=swap">
<style>
  :root{
    --stage:#161616;
    --white:#ffffff;
    --navy:#1d3f6e;
    --orange:#f5a623;
    --orange-deep:#e8901a;
    --brick:#b5553a;
    --brick-dark:#7d3524;
    --leaf:#5f8a3a;
    --leaf-light:#8fb85a;
    --taupe-light:#9a907a;
    --taupe-dark:#4d473a;
    --svc-white:#f4f4f4;
    --svc-yellow:#f7c325;
    --svc-green:#8cc63f;
    --svc-orange:#f39a1e;
    --svc-pink:#ec2e7b;
    --svc-cyan:#37c0d8;
    --bullet:#f7c325;
    --body:#2a3b55;
  }
  *{box-sizing:border-box;margin:0;padding:0}
  html,body{width:1200px;height:900px;overflow:hidden;background:var(--stage)}
  .canvas{position:relative;width:1200px;height:900px;display:flex;align-items:center;justify-content:center;gap:40px}
  .flyer{position:relative;width:540px;height:380px;overflow:hidden;box-shadow:0 10px 30px rgba(0,0,0,.6)}

  /* front */
  .photo{position:absolute}
  .front .wall-photo{inset:0;background:
      radial-gradient(ellipse at 70% 75%, var(--leaf) 0 22%, transparent 45%),
      radial-gradient(ellipse at 45% 30%, var(--leaf-light) 0 8%, transparent 26%),
      linear-gradient(135deg, var(--brick) 0%, #c46a4c 45%, var(--brick-dark) 100%)}
  .front .lower-panel{position:absolute;left:0;bottom:0;width:100%;height:220px}
  .front .ring{position:absolute;left:330px;top:70px;width:92px;height:92px;border-radius:50%;border:11px solid #e9eef2;background:radial-gradient(circle,#4c6e34,#2f4a22);box-shadow:0 2px 6px rgba(0,0,0,.35)}
  .brand-disc{position:absolute;border-radius:50%;background:var(--white);border:3px solid var(--leaf-light);display:flex;flex-direction:column;align-items:center;justify-content:center;text-align:center;font-family:"Open Sans",sans-serif;color:var(--navy);font-weight:700}
  .front .brand-disc{left:40px;top:60px;width:140px;height:140px;font-size:18px;line-height:1.15}
  .brand-name{display:block}
  .intro{position:absolute;left:40px;top:232px;width:310px;font-family:"Open Sans",sans-serif;font-size:11.5px;line-height:1.4;color:var(--body)}
  .thumbs{position:absolute;left:18px;bottom:14px;display:flex;gap:14px}
  .thumb{width:70px;height:52px;border:3px solid var(--white);box-shadow:0 1px 4px rgba(0,0,0,.35)}
  .thumb.t1{background:linear-gradient(#6f9a48,#3f6a2e)}
  .thumb.t2{background:linear-gradient(#9bb57a,#5d7d3e)}
  .thumb.t3{background:linear-gradient(#d89bb8,#6a9a47)}
  .thumb.t4{background:linear-gradient(#c9a98a,#8a6e52)}
  .thumb.t5{background:linear-gradient(#e6e1d6,#b3583d)}

  /* back */
  .back .backdrop{position:absolute;inset:0;background:radial-gradient(ellipse at 60% 35%, var(--taupe-light) 0%, #7a715e 40%, var(--taupe-dark) 100%)}
  .back .garden-photo{left:0;right:0;bottom:0;height:170px;background:
      radial-gradient(ellipse at 15% 85%, var(--leaf) 0 25%, transparent 45%),
      radial-gradient(ellipse at 85% 20%, #e9e6df 0 14%, transparent 30%),
      linear-gradient(160deg, transparent 0 8%, var(--brick) 30%, #c46a4c 60%, var(--brick-dark) 100%);
      -webkit-mask-image:linear-gradient(to bottom,transparent,#000 35%);mask-image:linear-gradient(to bottom,transparent,#000 35%)}
  .services{position:absolute;left:22px;top:16px;list-style:none;font-family:"Lilita One",sans-serif;font-size:22px;line-height:1.18;letter-spacing:.5px}
  .services li{display:flex;align-items:center;gap:9px;text-shadow:0 2px 2px rgba(0,0,0,.55)}
  .services li::before{content:"";width:9px;height:9px;border-radius:50%;background:var(--bullet);flex:none}
  .svc-white{color:var(--svc-white)}
  .svc-yellow{color:var(--svc-yellow)}
  .svc-green{color:var(--svc-green)}
  .svc-orange{color:var(--svc-orange)}
  .svc-pink{color:var(--svc-pink)}
  .svc-cyan{color:var(--svc-cyan)}
  .back .brand-disc{left:340px;top:100px;width:170px;height:170px;border-width:4px;font-size:16px;line-height:1.15;padding:0 14px;box-shadow:0 0 20px rgba(255,255,255,.35)}
  .contact{margin-top:8px;font-size:9.5px;font-weight:600;line-height:1.35;text-align:left;font-style:normal}
  .contact .lead{font-weight:700;font-size:10px}
</style>
</head>
<body>
<main class="canvas">

  <section class="flyer front" aria-label="Flyer front">
    <div class="photo wall-photo" role="img" aria-label="Photo of a red brick garden wall with hanging flower baskets and green shrubs"></div>
    <div class="ring" role="img" aria-label="Round window in the wall showing garden greenery"></div>
    <svg class="lower-panel" viewBox="0 0 540 220" preserveAspectRatio="none" aria-hidden="true">
      <path d="M0 40 C160 28 330 40 400 62 C450 78 480 130 500 220 L0 220 Z" fill="var(--white)"/>
      <path d="M400 62 C455 78 490 120 512 220 L540 220 L540 175 C520 125 475 75 400 62 Z" fill="var(--orange)"/>
      <path d="M0 40 C40 36 70 33 100 31 L100 46 C60 48 30 51 0 56 Z" fill="var(--orange-deep)"/>
    </svg>
    <div class="brand-disc">
      <span class="brand-name">Stonvale</span>
      <span class="brand-name">Building Services</span>
    </div>
    <p class="intro">Stonvale Building Services is a Marlow Heath based company covering Northmere, Westvale and the Eastbrook areas.</p>
    <div class="thumbs">
      <div class="thumb t1" role="img" aria-label="Photo of a garden with decking"></div>
      <div class="thumb t2" role="img" aria-label="Photo of a landscaped garden path"></div>
      <div class="thumb t3" role="img" aria-label="Photo of a flower bed on a lawn"></div>
      <div class="thumb t4" role="img" aria-label="Photo of timber fencing"></div>
      <div class="thumb t5" role="img" aria-label="Photo of a brick conservatory"></div>
    </div>
  </section>

  <section class="flyer back" aria-label="Flyer back">
    <div class="backdrop"></div>
    <div class="photo garden-photo" role="img" aria-label="Photo of a brick wall with flower baskets, shrubs and a white pillar"></div>
    <ul class="services">
      <li class="svc-white">PATIOS &amp; DECKING</li>
      <li class="svc-yellow">GARAGE CONVERTIONS</li>
      <li class="svc-green">EXTENSIONS</li>
      <li class="svc-orange">FENCHING</li>
      <li class="svc-pink">BRICK WALL</li>
      <li class="svc-white">DRIVEWAYS</li>
      <li class="svc-cyan">CONSERVATORIES</li>
      <li class="svc-white">FASCIAS &amp; SOFFITS</li>
      <li class="svc-yellow">GUTTERING</li>
      <li class="svc-pink">PROPERY ALTERATIONS</li>
    </ul>
    <div class="brand-disc">
      <span class="brand-name">Stonvale Building Services</span>
      <address class="contact">
        <span class="lead">CONTACT DERMOT</span><br>
        Email: info@stonvale.co.uk<br>
        Web: www.stonvale.co.uk<br>
        Tel: 01632 960481<br>
        Mob: 07700 900318
      </address>
    </div>
  </section>

</main>
</body>
</html>
```